Landfill Gas-to-Renewable Natural Gas business

We have a website ( coralbayfuelworks .com via Net Burrow) that needs to be revamped.

We have three RNG projects in Puerto Rico (Humacao, Ponce, Salinas), that take landfill gas (LFG) and produce renewable liquid natural gas (R-LNG) for companies looking to offset their carbon emissions (footprint). We also produce a renewable carbon dioxide (R-CO2) that can be reused for industrial CO2 purposes. All CO2 is imported to the island, so reusing CO2 on the island further reduces global CO2 emissions. The design should reflect renewables, sustainability, professionalism, safety and experience in this sector.

Sites with RNG examples:
https://www.qz.com/en_us/united-states/home/what-we-do/production-and-operations/velmora-power.html
https://tidefuelplex.com/
http://brindlepower.com/operations/
https://quillgases.com/
https://www.zentorgas.com/
https://harlowgas.com/
https://pinecrestfuelworks.com/
https://stokegas.com/
https://www.vontella.com/renewable-natural-gas/
https://www.kelbyfuelsystems.com/

Industry/Entity Type

Renewables Natural Gas, Sustainability,

Coding

Coded - Design and coding required

Number of Pages Required

4 page

Requirements
Must have
• Health, Safety, Environment (HSE) aspect. Industry experience section, about us, photos, landfill gas, LNG, RNG, CO2

```html
<!DOCTYPE html>
<html lang="en">
<head>
<meta charset="utf-8">
<title>Coral Bay Fuelworks</title>
<link rel="stylesheet" href="https://fonts.googleapis.com/css2?family=Poppins:wght@400;500;600&display=swap">
<style>
:root{
  --lime:#dcf50a;
  --lime-soft:#f5fbc8;
  --ink:#1d1d1d;
  --muted:#7a7a7a;
  --line:#e4e4e4;
  --panel:#eef2fb;
  --forest:#0a3a1d;
  --forest-text:#9cc62c;
  --white:#ffffff;
}
*{box-sizing:border-box;margin:0;padding:0}
html,body{width:1200px;height:4694px;overflow:hidden}
body{font-family:"Poppins",sans-serif;color:var(--ink);background:var(--white);position:relative}
.tag{position:absolute;height:33px;padding:0 16px;border-radius:17px;background:var(--lime-soft);border:1px solid #e8f29a;font-size:12px;font-weight:500;line-height:31px;text-transform:uppercase}
.btn-lime{position:absolute;background:var(--lime);border-radius:30px;font-size:13px;font-weight:500;display:flex;align-items:center;justify-content:center;gap:8px;color:var(--ink)}
.arrow{width:12px;height:12px}
.hero{position:absolute;left:0;top:0;width:1200px;height:730px;overflow:hidden}
.hero-photo{position:absolute;inset:0;background:linear-gradient(180deg,#3f86cf 0%,#7fb4e4 38%,#b9d4ea 52%,#3d6f9f 58%,#1e4f86 100%)}
.logo{position:absolute;display:flex;align-items:center;gap:8px;font-size:20px;font-weight:600;color:var(--white);line-height:24px}
.logo .dot{width:12px;height:12px;border-radius:50%;background:var(--white)}
.nav{position:absolute;left:464px;top:32px;display:flex;gap:20px;font-size:13px;color:var(--white)}
.nav a{color:inherit;text-decoration:none}
.hero h1{position:absolute;left:0;width:1200px;top:162px;text-align:center;color:var(--white);font-size:44px;font-weight:600;line-height:50px}
.hero-lead{position:absolute;left:260px;width:680px;top:282px;text-align:center;color:var(--white);font-size:13px;line-height:16px}
.glass{position:absolute;left:428px;top:477px;width:346px;height:171px;border-radius:14px;background:rgba(255,255,255,.22);border:2px solid rgba(255,255,255,.55);padding:18px 14px;color:var(--white)}
.glass h3{font-size:16px;font-weight:500;line-height:20px}
.glass p{font-size:12px;line-height:15px;margin-top:6px}
.glass .go{position:absolute;left:14px;bottom:18px;width:36px;height:36px;border-radius:50%;background:var(--lime);display:flex;align-items:center;justify-content:center}
.about-title{position:absolute;left:64px;top:912px;font-size:26px;font-weight:500}
.about-copy{position:absolute;left:64px;top:950px;width:400px;font-size:16px;line-height:27px;color:#333}
.about-copy p+p{margin-top:27px}
.btn-outline{position:absolute;left:64px;top:1275px;width:143px;height:52px;border:1.5px solid var(--ink);border-radius:26px;font-size:13px;display:flex;align-items:center;justify-content:center;gap:6px}
.about-photo{position:absolute;left:483px;top:814px;width:375px;height:539px;border-radius:12px;background:linear-gradient(160deg,#5b9be0 0%,#a8cdf1 55%,#e6eef6 100%)}
.dots{position:absolute;left:636px;top:1316px;display:flex;gap:6px}
.dots i{width:8px;height:8px;border-radius:50%;background:rgba(255,255,255,.7)}
.dots i:first-child{background:var(--lime)}
.note{position:absolute;background:var(--panel);border-radius:12px;padding:16px;font-size:12.5px;line-height:15.5px;color:#222}
.note p+p{margin-top:15px}
.section-title{position:absolute;left:64px;font-size:26px;font-weight:500}
.card{position:absolute;top:1593px;width:249px;height:356px;border:1.5px solid var(--line);border-radius:12px;padding:20px 18px}
.card svg{width:48px;height:48px}
.card h3{font-size:19px;font-weight:500;line-height:25px;margin-top:8px}
.card p{font-size:12.5px;line-height:21.5px;color:var(--muted);margin-top:10px}
.map{position:absolute;left:64px;top:2103px;width:1074px;height:501px;border-radius:40px;background:radial-gradient(ellipse at 55% 45%,#dde5e8 0%,#eef2f3 55%,#ffffff 80%)}
.pin{position:absolute;display:flex;flex-direction:column;align-items:center;font-size:10px;font-weight:500}
.pin svg{width:20px;height:24px}
.test-title{position:absolute;left:0;width:1200px;top:2843px;text-align:center;font-size:40px;font-weight:500;line-height:47px}
.quote-card{position:absolute;top:8px;width:430px;height:273px;border:1.5px solid var(--line);border-radius:12px;padding:22px 18px}
.quote-card h3{font-size:16px;font-weight:500;line-height:21px;margin-top:14px}
.quote-card p{font-size:13px;line-height:22px;color:#333;margin-top:12px}
.stars{display:flex;gap:6px;margin-top:10px}
.stars svg{width:15px;height:15px}
.author{display:flex;align-items:center;gap:10px;margin-top:10px;font-size:16px}
.author i{width:30px;height:30px;border-radius:50%;background:#9aa6b5}
.clip{position:absolute;left:0;top:2980px;width:1200px;height:300px;overflow:hidden}
.circ{position:absolute;top:3312px;width:68px;height:68px;border-radius:50%;display:flex;align-items:center;justify-content:center}
.post{position:absolute;top:3551px;width:338px;height:392px;border:1.5px solid var(--line);border-radius:12px;padding:18px}
.post .ph{height:216px;border-radius:4px}
.post h3{font-size:16px;font-weight:500;margin-top:12px}
.post p{font-size:12.5px;line-height:21.5px;color:var(--muted);margin-top:8px;width:200px}
.band{position:absolute;left:0;top:4028px;width:1200px;height:666px;background:var(--forest)}
.band-rule{position:absolute;left:0;top:4298px;width:1200px;height:1px;background:rgba(255,255,255,.15)}
.sub-title{position:absolute;left:0;width:1200px;top:4075px;text-align:center;font-size:32px;font-weight:600;color:var(--forest-text)}
.sub-lead{position:absolute;left:240px;width:720px;top:4140px;text-align:center;font-size:13px;line-height:22px;color:var(--white)}
.field{position:absolute;left:364px;top:4203px;width:321px;height:53px;border-radius:27px;background:#e6e6e6;font-size:11px;color:#8a8a8a;padding:0 22px;line-height:53px}
.foot{color:var(--white);position:absolute}
.foot h4{font-size:20px;font-weight:500}
.foot ul{list-style:none;font-size:13px;line-height:30px;margin-top:12px}
.social{position:absolute;left:66px;top:4613px;display:flex;align-items:center;gap:10px;color:var(--white);font-size:13px}
.social i{width:32px;height:32px;border-radius:50%;border:1.5px solid var(--white)}
</style>
</head>
<body>

<section class="hero">
  <div class="hero-photo" role="img" aria-label="Landfill gas processing plant on the Puerto Rico coast under a blue sky"></div>
  <div class="logo" style="left:64px;top:28px"><span class="dot"></span>Coral Bay Fuelworks</div>
  <nav class="nav"><a href="#">About</a><a href="#">Solutions</a><a href="#">Project</a><a href="#">Industries</a></nav>
  <a class="btn-lime" style="left:1020px;top:22px;width:125px;height:38px">Contact us <svg class="arrow" viewBox="0 0 12 12"><path d="M2 10L10 2M4 2h6v6" fill="none" stroke="#1d1d1d" stroke-width="1.4"/></svg></a>
  <h1>Turning landfill gas<br>into renewable natural gas.</h1>
  <p class="hero-lead">Coral Bay Fuelworks is a Puerto Rico renewable natural gas business. We capture landfill gas and produce renewable LNG and renewable CO2 at three projects on the island.</p>
  <a class="btn-lime" style="left:495px;top:364px;width:208px;height:48px;font-size:12px">GET A FREE QUOTE <svg class="arrow" viewBox="0 0 12 12"><path d="M2 10L10 2M4 2h6v6" fill="none" stroke="#1d1d1d" stroke-width="1.4"/></svg></a>
  <div class="glass">
    <h3>Renewable Fuel from<br>Landfill Gas in Puerto Rico</h3>
    <p>We help companies offset their carbon footprint with renewable LNG made from captured landfill gas.</p>
    <span class="go"><svg class="arrow" viewBox="0 0 12 12"><path d="M2 10L10 2M4 2h6v6" fill="none" stroke="#1d1d1d" stroke-width="1.4"/></svg></span>
  </div>
</section>

<span class="tag" style="left:64px;top:843px">About us</span>
<h2 class="about-title">About us</h2>
<div class="about-copy">
  <p>Coral Bay Fuelworks was founded by an experienced team of gas and energy engineers to turn landfill gas into clean fuel for Puerto Rico.</p>
  <p>Our three projects in Humacao, Ponce and Salinas capture methane that would escape into the air and convert it into renewable LNG and renewable CO2 for island industry.</p>
</div>
<a class="btn-outline">Learn More <svg class="arrow" viewBox="0 0 12 12"><path d="M2 10L10 2M4 2h6v6" fill="none" stroke="#1d1d1d" stroke-width="1.4"/></svg></a>
<div class="about-photo" role="img" aria-label="Landfill gas wellheads and pipework at a project site"></div>
<div class="dots"><i></i><i></i><i></i><i></i></div>
<div class="note" style="left:876px;top:814px;width:282px;height:222px">
  <p>Our objective is to help companies lower their carbon footprint by supplying renewable LNG produced from landfill gas, with full tracking from wellhead to delivery.</p>
  <p>All CO2 used in Puerto Rico is imported. By capturing and reusing renewable CO2 on the island, we further reduce global CO2 emissions.</p>
</div>
<div class="note" style="left:783px;top:1082px;width:279px;height:235px">
  <p>Health, safety and the environment come first. Every site runs to strict HSE standards with trained crews, gas detection and regular audits.</p>
  <p>Our team brings decades of industry experience in landfill gas collection, gas upgrading, liquefaction and CO2 recovery, and we work closely with local communities and agencies.</p>
</div>

<span class="tag" style="left:64px;top:1439px">Services</span>
<h2 class="section-title" style="top:1515px">Our Solutions</h2>
<a class="btn-lime" style="left:989px;top:1508px;width:147px;height:51px">View More <svg class="arrow" viewBox="0 0 12 12"><path d="M2 10L10 2M4 2h6v6" fill="none" stroke="#1d1d1d" stroke-width="1.4"/></svg></a>

<div class="card" style="left:64px">
  <svg viewBox="0 0 48 48" fill="none" stroke="#1d1d1d" stroke-width="2"><path d="M4 40h40M10 40V24h8v16M14 24V12M30 40V20h8v20M34 20V8"/><path d="M18 30h12"/></svg>
  <h3>Landfill Gas<br>Capture</h3>
  <p>We collect methane-rich landfill gas through a network of wells and pipes, stopping it from escaping into the air and turning a waste stream into a dependable source of renewable energy for the island.</p>
</div>
<div class="card" style="left:337px">
  <svg viewBox="0 0 48 48" fill="none" stroke="#1d1d1d" stroke-width="2"><path d="M24 4c8 10 12 17 12 24a12 12 0 01-24 0c0-7 4-14 12-24z"/><path d="M24 22c3 4 5 7 5 10a5 5 0 01-10 0c0-3 2-6 5-10z"/></svg>
  <h3>Renewable LNG<br>Production</h3>
  <p>Cleaned and upgraded landfill gas is liquefied into renewable LNG, giving companies a practical low-carbon fuel that offsets their emissions and fits into existing natural gas equipment.</p>
</div>
<div class="card" style="left:612px">
  <svg viewBox="0 0 48 48" fill="none" stroke="#1d1d1d" stroke-width="2"><rect x="14" y="10" width="20" height="32" rx="6"/><path d="M20 10V5h8v5"/><path d="M20 26a4 4 0 108 0M24 30v4"/></svg>
  <h3>Renewable CO2<br>Recovery</h3>
  <p>We recover renewable CO2 from the gas stream for reuse in industrial CO2 applications. As all CO2 is imported, local supply cuts shipping and lowers global CO2 emissions.</p>
</div>
<div class="card" style="left:887px">
  <svg viewBox="0 0 48 48" fill="none" stroke="#1d1d1d" stroke-width="2" stroke-linejoin="round"><path d="M24 4l16 6v12c0 10-7 18-16 22-9-4-16-12-16-22V10z"/><path d="M17 24l5 5 9-10"/></svg>
  <h3>Health, Safety<br>and Environment</h3>
  <p>Our HSE program protects our people, neighbours and surroundings, with trained operators, continuous gas monitoring, emergency planning and regular audits at every project site we run.</p>
</div>

<span class="tag" style="left:555px;top:2034px">Projects</span>
<div class="map" role="img" aria-label="Dotted map of Puerto Rico showing project locations"></div>
<div class="pin" style="left:480px;top:2106px"><svg viewBox="0 0 20 24" fill="none" stroke="#333" stroke-width="1.4"><path d="M10 23s8-8 8-13a8 8 0 10-16 0c0 5 8 13 8 13z"/><circle cx="10" cy="10" r="3"/></svg>Humacao</div>
<div class="pin" style="left:503px;top:2164px"><svg viewBox="0 0 20 24" fill="none" stroke="#333" stroke-width="1.4"><path d="M10 23s8-8 8-13a8 8 0 10-16 0c0 5 8 13 8 13z"/><circle cx="10" cy="10" r="3"/></svg>Salinas</div>
<div class="pin" style="left:468px;top:2217px"><svg viewBox="0 0 20 24" fill="none" stroke="#333" stroke-width="1.4"><path d="M10 23s8-8 8-13a8 8 0 10-16 0c0 5 8 13 8 13z"/><circle cx="10" cy="10" r="3"/></svg>Ponce</div>

<span class="tag" style="left:541px;top:2804px">Testimonial</span>
<h2 class="test-title">Success Stories from our Renewable<br>Fuel Customers</h2>
<div class="clip">
  <div class="quote-card" style="left:64px">
    <svg width="34" height="26" viewBox="0 0 34 26" fill="none" stroke="#1d1d1d" stroke-width="2.4"><circle cx="8" cy="17" r="6"/><path d="M4 13L12 3"/><circle cx="25" cy="17" r="6"/><path d="M21 13l8-10"/></svg>
    <h3>Switching to renewable LNG was a turning point for us</h3>
    <p>Working with Delwyn's team was a game-changer. Their renewable LNG cut our reported emissions, and deliveries have been safe and on time.</p>
    <div class="stars"><svg viewBox="0 0 20 20"><path d="M10 1l2.7 6 6.3.6-4.8 4.2 1.4 6.4L10 15l-5.6 3.2 1.4-6.4L1 7.6 7.3 7z" fill="#e7c800"/></svg><svg viewBox="0 0 20 20"><path d="M10 1l2.7 6 6.3.6-4.8 4.2 1.4 6.4L10 15l-5.6 3.2 1.4-6.4L1 7.6 7.3 7z" fill="#e7c800"/></svg><svg viewBox="0 0 20 20"><path d="M10 1l2.7 6 6.3.6-4.8 4.2 1.4 6.4L10 15l-5.6 3.2 1.4-6.4L1 7.6 7.3 7z" fill="#e7c800"/></svg><svg viewBox="0 0 20 20"><path d="M10 1l2.7 6 6.3.6-4.8 4.2 1.4 6.4L10 15l-5.6 3.2 1.4-6.4L1 7.6 7.3 7z" fill="#e7c800"/></svg><svg viewBox="0 0 20 20"><path d="M10 1l2.7 6 6.3.6-4.8 4.2 1.4 6.4L10 15l-5.6 3.2 1.4-6.4L1 7.6 7.3 7z" fill="#e7c800"/></svg></div>
    <div class="author"><i role="img" aria-label="Customer portrait"></i>Rowan Ellery</div>
  </div>
  <div class="quote-card" style="left:521px">
    <svg width="34" height="26" viewBox="0 0 34 26" fill="none" stroke="#1d1d1d" stroke-width="2.4"><circle cx="8" cy="17" r="6"/><path d="M4 13L12 3"/><circle cx="25" cy="17" r="6"/><path d="M21 13l8-10"/></svg>
    <h3>Local renewable CO2 changed our supply chain</h3>
    <p>Buying renewable CO2 made here on the island means shorter lead times and a lower footprint. Their HSE standards give us full confidence.</p>
    <div class="stars"><svg viewBox="0 0 20 20"><path d="M10 1l2.7 6 6.3.6-4.8 4.2 1.4 6.4L10 15l-5.6 3.2 1.4-6.4L1 7.6 7.3 7z" fill="#e7c800"/></svg><svg viewBox="0 0 20 20"><path d="M10 1l2.7 6 6.3.6-4.8 4.2 1.4 6.4L10 15l-5.6 3.2 1.4-6.4L1 7.6 7.3 7z" fill="#e7c800"/></svg><svg viewBox="0 0 20 20"><path d="M10 1l2.7 6 6.3.6-4.8 4.2 1.4 6.4L10 15l-5.6 3.2 1.4-6.4L1 7.6 7.3 7z" fill="#e7c800"/></svg><svg viewBox="0 0 20 20"><path d="M10 1l2.7 6 6.3.6-4.8 4.2 1.4 6.4L10 15l-5.6 3.2 1.4-6.4L1 7.6 7.3 7z" fill="#e7c800"/></svg><svg viewBox="0 0 20 20"><path d="M10 1l2.7 6 6.3.6-4.8 4.2 1.4 6.4L10 15l-5.6 3.2 1.4-6.4L1 7.6 7.3 7z" fill="#e7c800"/></svg></div>
    <div class="author"><i role="img" aria-label="Customer portrait" style="background:#56677e"></i>Rowan Ellery</div>
  </div>
  <div class="quote-card" style="left:978px">
    <svg width="34" height="26" viewBox="0 0 34 26" fill="none" stroke="#1d1d1d" stroke-width="2.4"><circle cx="8" cy="17" r="6"/><path d="M4 13L12 3"/><circle cx="25" cy="17" r="6"/><path d="M21 13l8-10"/></svg>
    <h3>Switching to renewable LNG was a turning point for us</h3>
    <p>Working with Delwyn's team was a game-changer. Their renewable LNG cut our reported emissions, and deliveries have been safe and on time.</p>
    <div class="stars"><svg viewBox="0 0 20 20"><path d="M10 1l2.7 6 6.3.6-4.8 4.2 1.4 6.4L10 15l-5.6 3.2 1.4-6.4L1 7.6 7.3 7z" fill="#e7c800"/></svg><svg viewBox="0 0 20 20"><path d="M10 1l2.7 6 6.3.6-4.8 4.2 1.4 6.4L10 15l-5.6 3.2 1.4-6.4L1 7.6 7.3 7z" fill="#e7c800"/></svg><svg viewBox="0 0 20 20"><path d="M10 1l2.7 6 6.3.6-4.8 4.2 1.4 6.4L10 15l-5.6 3.2 1.4-6.4L1 7.6 7.3 7z" fill="#e7c800"/></svg><svg viewBox="0 0 20 20"><path d="M10 1l2.7 6 6.3.6-4.8 4.2 1.4 6.4L10 15l-5.6 3.2 1.4-6.4L1 7.6 7.3 7z" fill="#e7c800"/></svg><svg viewBox="0 0 20 20"><path d="M10 1l2.7 6 6.3.6-4.8 4.2 1.4 6.4L10 15l-5.6 3.2 1.4-6.4L1 7.6 7.3 7z" fill="#e7c800"/></svg></div>
    <div class="author"><i role="img" aria-label="Customer portrait" style="background:#c9a27e"></i>Rowan Ellery</div>
  </div>
</div>
<span class="circ" style="left:523px;border:1.5px solid #bdbdbd"><svg width="18" height="12" viewBox="0 0 18 12" fill="none" stroke="#1d1d1d" stroke-width="1.5"><path d="M17 6H2M6 1L1 6l5 5"/></svg></span>
<span class="circ" style="left:607px;background:var(--lime)"><svg width="18" height="12" viewBox="0 0 18 12" fill="none" stroke="#1d1d1d" stroke-width="1.5"><path d="M1 6h15M12 1l5 5-5 5"/></svg></span>

<h2 class="section-title" style="top:3473px">Blog &amp; News</h2>
<a class="btn-lime" style="left:989px;top:3465px;width:147px;height:51px">View More <svg class="arrow" viewBox="0 0 12 12"><path d="M2 10L10 2M4 2h6v6" fill="none" stroke="#1d1d1d" stroke-width="1.4"/></svg></a>
<article class="post" style="left:64px">
  <div class="ph" role="img" aria-label="Landfill site with gas flare at sunset" style="background:linear-gradient(180deg,#3b2a2a 0%,#c9582a 55%,#f2a33a 70%,#3a2418 100%)"></div>
  <h3>What Is Landfill Gas?</h3>
  <p>How methane from waste becomes a steady source of renewable fuel for Puerto Rico.</p>
</article>
<article class="post" style="left:430px">
  <div class="ph" role="img" aria-label="Renewable LNG storage tanks under a clear sky" style="background:linear-gradient(180deg,#4d86d6 0%,#8fb6ea 30%,#2c4fa8 45%,#1e3a86 100%)"></div>
  <h3>Renewable LNG Explained</h3>
  <p>Why renewable LNG helps companies offset their carbon footprint without new equipment.</p>
</article>
<article class="post" style="left:796px">
  <div class="ph" role="img" aria-label="Gas processing units at a project site under a grey sky" style="background:linear-gradient(180deg,#b7c2c9 0%,#d2d9dd 55%,#3d4a48 75%,#1f2a28 100%)"></div>
  <h3>Reusing CO2 on the Island</h3>
  <p>Local renewable CO2 replaces imports and lowers global CO2 emissions for industry.</p>
</article>

<div class="band"></div>
<div class="band-rule"></div>
<h2 class="sub-title">SUBSCRIBE NOW TO GET STARTED</h2>
<p class="sub-lead">Subscribe now to follow our renewable natural gas projects. Get news on renewable LNG, renewable CO2 and our safety record in Puerto Rico.</p>
<div class="field">Enter Email</div>
<a class="btn-lime" style="left:694px;top:4203px;width:140px;height:53px">Subscribe <svg class="arrow" viewBox="0 0 12 12"><path d="M2 10L10 2M4 2h6v6" fill="none" stroke="#1d1d1d" stroke-width="1.4"/></svg></a>

<div class="logo" style="left:66px;top:4352px"><span class="dot"></span>Coral Bay Fuelworks</div>
<p class="foot" style="left:66px;top:4410px;width:280px;font-size:13px;line-height:22px">Coral Bay Fuelworks turns landfill gas into renewable LNG and renewable CO2 at three projects in Humacao, Ponce and Salinas, Puerto Rico.</p>
<div class="foot" style="left:603px;top:4345px">
  <h4>Quick Link</h4>
  <ul><li>About</li><li>Solutions</li><li>Projects</li><li>HSE</li></ul>
</div>
<div class="foot" style="left:951px;top:4345px;width:200px">
  <h4>Contact</h4>
  <ul><li>info@coralbayfuelworks.com</li></ul>
  <p style="font-size:13px;line-height:22px;margin-top:6px">Head Office, Suite 4 Marina Business Centre, Calle Vela, Ponce, PR 00717</p>
</div>
<div class="social">Social Links <i></i><i></i><i></i></div>
<p class="foot" style="left:830px;width:303px;top:4621px;text-align:right;font-size:12px;color:#b9c4bd">©2025 Coral Bay Fuelworks</p>

</body>
</html>
```